Buch-/eBook-Cover für Autobiografie
Das Disign von dem Cover hat mir auf Anhieb sehr gut gefallen. Das hat gleich "ins schwarze" getroffen. Die Kommunikation war effizient und zielgerichtet
Zielgruppe
Ich bin eine Privatperson und habe im Laufe der letzten Jahre mein Autobiografie geschrieben. Besser gesagt ist es ein autobiografischer Roman geworden. Ich plane dieses Buch meiner Frau und meinen Söhnen und deren Familien zu schenken. Darüber hinaus ist es aber auch geplant das Buch bei Veltaro zu veröffentlichen.
Aufgabenstellung
Auf dem Cover sollte neben meinem Namen Konrad(a) Pelzmann natürlich auch der Titel von dem Buch stehen. Ich habe dem Buch den Titel gegeben: 'Das Licht am Ufer'. Auf dem Backcover hatte ich mir eine kurze zusammenfassung vorgestellt, die ich auch beifüge. Ich hatte geplant, das sowohl auf dem Cover, wie auch auf dem Backcover Bilder von mir (u.a. als Baby) mit gestaltet werden. Aber das ist nur so eine Idee, ich bin da für Vorschläge offen
Das Design darf nicht zu überladen sein.

```html
<!DOCTYPE html>
<html lang="de">
<head>
<meta charset="utf-8">
<title>Das Licht am Ufer – Buchumschlag</title>
<link href="https://fonts.googleapis.com/css2?family=Marcellus&family=Playfair+Display:ital,wght@0,500;1,700&family=Arimo:wght@700&display=swap" rel="stylesheet">
<style>
  :root {
    --paper: #ecdcc1;
    --paper-front: #eadbbf;
    --spine: #efe3cb;
    --fold: rgba(120, 95, 60, 0.12);
    --ink: #191613;
    --ink-soft: #5a534b;
    --gold-light: #e2c98f;
    --photo-dark: #2a2a2a;
    --photo-mid: #8d8d8d;
    --photo-light: #d6d6d6;
  }
  html, body { margin: 0; padding: 0; overflow: hidden; }
  body { width: 1200px; height: 899px; background: var(--paper); }
  .cover-spread {
    position: relative; width: 1200px; height: 899px; overflow: hidden;
    background: linear-gradient(90deg, var(--paper) 0 548px, var(--spine) 548px 642px, var(--paper-front) 642px);
  }
  .fold { position: absolute; top: 0; bottom: 0; width: 1px; background: var(--fold); }
  .back-cover { position: absolute; left: 96px; top: 100px; width: 392px; font-family: "Marcellus", serif; color: var(--ink-soft); font-size: 15px; line-height: 20px; }
  .back-cover p { margin: 0 0 14px; }
  .back-cover .lead { margin-bottom: 10px; }
  .back-cover .subhead { font-size: 13px; margin-bottom: 4px; }
  .back-cover .gap { margin-top: 40px; }
  .tagline { position: absolute; left: 96px; top: 792px; font-family: "Marcellus", serif; font-size: 10px; letter-spacing: 0.4px; color: var(--ink); }
  .spine-title {
    position: absolute; left: 578px; top: 78px; writing-mode: vertical-rl;
    font-family: "Playfair Display", serif; font-weight: 500; font-size: 27px; letter-spacing: 3px; color: var(--ink);
  }
  .title-top { position: absolute; left: 782px; top: 52px; font-family: "Playfair Display", serif; font-style: italic; font-weight: 700; font-size: 62px; color: var(--ink); margin: 0; }
  .title-main { position: absolute; left: 760px; top: 118px; font-family: "Playfair Display", serif; font-weight: 500; font-size: 60px; letter-spacing: -1px; color: var(--ink); margin: 0; }
  .title-bottom { position: absolute; left: 735px; top: 693px; font-family: "Playfair Display", serif; font-weight: 500; font-size: 64px; letter-spacing: -1px; color: var(--ink); margin: 0; }
  .author { position: absolute; left: 792px; top: 789px; font-family: "Arimo", sans-serif; font-weight: 700; font-size: 20px; color: var(--ink); margin: 0; }
  .portrait {
    position: absolute; width: 164px; height: 158px; border: 4px solid var(--gold-light);
    box-shadow: 3px 5px 10px rgba(60, 40, 10, 0.35);
  }
  .portrait-baby { left: 832px; top: 203px; transform: rotate(-3deg); background: radial-gradient(circle at 50% 45%, var(--photo-light), var(--photo-mid) 70%, var(--photo-dark)); }
  .portrait-child { left: 830px; top: 368px; transform: rotate(-3deg); background: radial-gradient(circle at 50% 50%, var(--photo-light), var(--photo-mid) 60%, #4a4a4a); }
  .portrait-adult { left: 795px; top: 526px; width: 168px; height: 160px; transform: rotate(3deg); background: radial-gradient(circle at 50% 45%, #b8b8b8, #555 55%, #111); }
</style>
</head>
<body>
<main class="cover-spread">
  <div class="fold" style="left:496px"></div>
  <div class="fold" style="left:548px"></div>
  <div class="fold" style="left:642px"></div>
  <div class="fold" style="left:692px"></div>

  <section class="back-cover">
    <p class="lead">Mit siebzig Jahren blickt ein Mann auf sein Leben zurück und beginnt, die alten Geschichten aufzuschreiben.</p>
    <p class="subhead">Zwischen Ufer und Horizont.</p>
    <p>Er erzählt von einer Kindheit am Fluss, von den ersten Schritten im Sand und von einem Vater, der ihm das Schwimmen beibrachte. Er erzählt von Freundschaften, die Jahrzehnte überdauerten, von Umwegen, von Arbeit in fremden Städten und von der Liebe, die ihn schließlich zurück nach Hause führte. Jede Erinnerung wird zu einem Stein auf dem Weg.</p>
    <p>Doch das Buch ist mehr als ein Rückblick. Es ist ein Gespräch zwischen dem Kind von damals und dem Mann von heute: über Verlust und Hoffnung, über Familie und Herkunft, über die Frage, was von einem Leben bleibt, wenn man es erzählt. Ein stiller, ehrlicher Roman für alle, die wissen wollen, woher sie kommen.</p>
    <p class="gap">Ein Geschenk an die eigene Familie und an jeden Leser, der spürt, dass die Vergangenheit nie ganz vergeht. Sie leuchtet weiter, wie ein Licht am Ufer, das den Weg zurück zeigt.</p>
  </section>
  <div class="tagline">EINE LEBENSGESCHICHTE ZWISCHEN ERINNERUNG UND GEGENWART</div>

  <div class="spine-title">DAS LICHT AM UFER</div>

  <p class="title-top">Das</p>
  <p class="title-main">LICHT AM</p>

  <div class="portrait portrait-baby" role="img" aria-label="Schwarzweißfoto des Autors als lächelndes Baby"></div>
  <div class="portrait portrait-child" role="img" aria-label="Schwarzweißfoto des Autors als Kleinkind"></div>
  <div class="portrait portrait-adult" role="img" aria-label="Schwarzweißporträt des Autors heute"></div>

  <p class="title-bottom">UFER</p>
  <p class="author">KONRAD(A) PELZMANN</p>
</main>
</body>
</html>
```